Real Estate Business Cards

Looking for a clean, sharp and professional look for our Real Estate investment Fund that invests in Multi Family Apartment buildings.

Target Market(s)

Real Estate Fund

Industry/Entity Type

Real Estate

Contact Information for Business Card

Company Description: Real Estate Investment Fund
Company Name: RKW Holdings
Name: Marcus Olvane
Cell: (917) 482-0657
Email: marcus@rkwholdings-example.com
Website: www.rkwholdings-example.com
Address: 418, 9th Street, Brooklyn NY 11218

Colors

Designer to choose colors to be used in the design.

Requirements
Nice to have
• Colors to match logo

```html
<!DOCTYPE html>
<html lang="en">
<head>
<meta charset="utf-8">
<title>RKW Holdings – Business Cards</title>
<link href="https://fonts.googleapis.com/css2?family=Lato:wght@400;700;900&display=swap" rel="stylesheet">
<style>
  :root {
    --backdrop: #2b2c2e;
    --card: #0d0d0f;
    --brand-blue: #1f78c1;
    --ink-light: #e6e6e6;
    --rule: #1d3b56;
  }
  * { margin: 0; padding: 0; box-sizing: border-box; }
  html, body { width: 1200px; height: 970px; overflow: hidden; }
  body {
    background: var(--backdrop);
    font-family: "Lato", Arial, sans-serif;
    position: relative;
  }
  .card {
    position: absolute;
    left: 240px;
    width: 720px;
    height: 400px;
    background: var(--card);
    border-bottom: 5px solid var(--brand-blue);
    box-shadow: 0 12px 28px rgba(0,0,0,.55);
  }
  .card--front { top: 60px; }
  .card--back { top: 510px; }

  .brand {
    display: flex;
    align-items: center;
    gap: 16px;
    font-family: "Lato", Arial, sans-serif;
    font-weight: 400;
    color: var(--brand-blue);
    letter-spacing: 2px;
    text-transform: uppercase;
    white-space: nowrap;
  }
  .brand__mark {
    background: var(--brand-blue);
    flex: none;
  }

  .card--front .brand {
    position: absolute;
    left: 60px;
    top: 180px;
    font-size: 26px;
  }
  .card--front .brand__mark { width: 30px; height: 30px; }

  .front__divider {
    position: absolute;
    left: 355px;
    top: 80px;
    width: 1px;
    height: 240px;
    background: var(--rule);
  }

  .contact {
    position: absolute;
    left: 395px;
    top: 78px;
    color: var(--ink-light);
  }
  .contact__name {
    font-weight: 900;
    font-size: 30px;
    color: var(--brand-blue);
    line-height: 1;
  }
  .contact__title {
    font-size: 17px;
    margin-top: 4px;
  }
  .contact__company {
    font-size: 17px;
    color: var(--brand-blue);
    margin-top: 14px;
  }
  .contact__address {
    font-size: 17px;
    line-height: 1.3;
    font-style: normal;
  }
  .contact__lines {
    list-style: none;
    margin-top: 16px;
  }
  .contact__lines li {
    display: flex;
    align-items: center;
    gap: 12px;
    font-size: 16px;
    line-height: 1.75;
  }
  .contact__lines svg { width: 16px; height: 16px; flex: none; }

  .card--back .brand {
    position: absolute;
    left: 50%;
    top: 50%;
    transform: translate(-50%, -50%);
    font-size: 40px;
    gap: 24px;
  }
  .card--back .brand__mark { width: 60px; height: 60px; }
</style>
</head>
<body>

  <section class="card card--front">
    <div class="brand">
      <span class="brand__mark"></span>
      <span class="brand__name">RKW Holdings</span>
    </div>

    <div class="front__divider"></div>

    <div class="contact">
      <p class="contact__name">Marcus Olvane</p>
      <p class="contact__title">Founder &amp; CEO</p>
      <p class="contact__company">RKW Holdings</p>
      <address class="contact__address">418, 9th Street,<br>Brooklyn NY 11218</address>
      <ul class="contact__lines">
        <li>
          <svg viewBox="0 0 16 16" aria-hidden="true"><path fill="#1f78c1" d="M3.5 1.5l2.5 0 1 3.2-1.6 1.1a8 8 0 0 0 4.8 4.8l1.1-1.6 3.2 1v2.5c0 .8-.7 1.5-1.5 1.5C6.7 14 2 9.3 2 3c0-.8.7-1.5 1.5-1.5z"/></svg>
          (917) 482-0657
        </li>
        <li>
          <svg viewBox="0 0 16 16" aria-hidden="true"><rect x="1" y="3" width="14" height="10" fill="#1f78c1"/><path d="M1 3l7 5.5L15 3" fill="none" stroke="#0d0d0f" stroke-width="1.3"/></svg>
          marcus@rkwholdings-example.com
        </li>
        <li>
          <svg viewBox="0 0 16 16" aria-hidden="true"><g fill="none" stroke="#1f78c1" stroke-width="1.3"><circle cx="8" cy="8" r="6.5"/><ellipse cx="8" cy="8" rx="2.8" ry="6.5"/><path d="M1.5 8h13M2.5 4.8h11M2.5 11.2h11"/></g></svg>
          www.rkwholdings-example.com
        </li>
      </ul>
    </div>
  </section>

  <section class="card card--back">
    <div class="brand">
      <span class="brand__mark"></span>
      <span class="brand__name">RKW Holdings</span>
    </div>
  </section>

</body>
</html>
```